Brisa Pastry Mill Business card

We are empanada whole-sellers and I want a business card design with a picture of an empanada on it that also mentions first trial order FREE. our contact number 555-214-7093 our website www.brisapastry.example and business email Tobin@brisapastry.example

If you want any of our artwork please feel free to email me at the address above.

```html
<!DOCTYPE html>
<html lang="en">
<head>
<meta charset="utf-8">
<title>Brisa Pastry Mill – Business Card</title>
<link rel="stylesheet" href="https://fonts.googleapis.com/css2?family=Roboto+Slab:wght@400;600;700;800&display=swap">
<style>
  :root {
    --mustard: #e2b622;
    --mustard-dark: #a88a2a;
    --ink: #231f20;
    --paper: #ffffff;
    --pattern: #efefef;
    --pastry-light: #cdb28c;
    --pastry-dark: #b89a70;
  }
  * { margin: 0; padding: 0; box-sizing: border-box; }
  html, body { width: 1200px; height: 1000px; overflow: hidden; }
  body { position: relative; background: var(--paper); font-family: "Roboto Slab", Rockwell, Georgia, serif; color: var(--ink); }

  .stage-top { position: absolute; left: 0; top: 0; width: 1200px; height: 500px; background: var(--mustard); }

  .card { position: absolute; left: 298px; width: 603px; height: 372px; }
  .card-front { top: 64px; }
  .card-back { top: 548px; background: var(--mustard); }

  /* front */
  .front-texture { position: absolute; inset: 0; background: var(--pattern); }
  .ribbon { position: absolute; left: 35px; width: 533px; height: 10px; background: var(--mustard); }
  .ribbon-top { top: 41px; }
  .ribbon-bottom { top: 319px; }
  .ribbon-fold { position: absolute; width: 19px; height: 24px; background: var(--mustard-dark); }
  .fold-tl { left: 35px; top: 51px; clip-path: polygon(0 0, 100% 0, 100% 100%); }
  .fold-tr { left: 549px; top: 51px; clip-path: polygon(0 0, 100% 0, 0 100%); }
  .fold-bl { left: 35px; top: 295px; clip-path: polygon(100% 0, 100% 100%, 0 100%); }
  .fold-br { left: 549px; top: 295px; clip-path: polygon(0 0, 100% 100%, 0 100%); }
  .panel { position: absolute; left: 54px; top: 51px; width: 495px; height: 270px; background: var(--paper); }
  .edge-trim { position: absolute; left: 0; width: 100%; height: 10px; background: var(--ink); }
  .trim-top { top: 0; }
  .trim-bottom { bottom: 0; }
  .ornament { position: absolute; width: 32px; height: 32px; border-radius: 50%; background: var(--ink); }
  .orn-1 { left: 23px; top: 47px; }
  .orn-2 { left: 440px; top: 47px; }
  .orn-3 { left: 23px; top: 190px; }
  .orn-4 { left: 440px; top: 190px; }
  .brand-name { position: absolute; left: 0; width: 100%; top: 100px; text-align: center; font-size: 42px; font-weight: 800; line-height: 1; white-space: nowrap; }
  .tagline { position: absolute; left: 0; width: 100%; top: 169px; text-align: center; font-size: 15px; font-weight: 700; letter-spacing: 0.4px; line-height: 1; }

  /* back */
  .offer-lead { position: absolute; left: 0; width: 100%; top: 40px; text-align: center; font-size: 27px; font-weight: 400; line-height: 1; }
  .offer-free { position: absolute; left: 0; width: 100%; top: 64px; text-align: center; font-size: 90px; font-weight: 400; line-height: 1; }
  .pastry-art { position: absolute; left: 148px; top: 160px; width: 130px; height: 78px; background: linear-gradient(180deg, var(--pastry-light), var(--pastry-dark)); }
  .product { position: absolute; left: 290px; width: 200px; text-align: center; color: var(--paper); font-weight: 600; line-height: 1; white-space: nowrap; }
  .product-above { top: 170px; font-size: 11px; }
  .product-main { top: 188px; font-size: 21px; }
  .product-below { top: 217px; font-size: 11px; }
  .phone { position: absolute; left: 0; width: 100%; top: 258px; text-align: center; color: var(--paper); font-size: 21px; font-weight: 700; line-height: 1; }
  .social { position: absolute; left: 0; width: 100%; top: 288px; display: flex; flex-direction: column; align-items: center; gap: 6px; font-size: 12px; font-weight: 700; line-height: 1; }
  .social-mark { width: 22px; height: 22px; background: var(--ink); }
  .contact { position: absolute; top: 316px; font-size: 15px; line-height: 1; white-space: nowrap; }
  .contact-web { left: 36px; }
  .contact-mail { right: 35px; }
</style>
</head>
<body>
  <div class="stage-top"></div>

  <section class="card card-front">
    <div class="front-texture" role="img" aria-label="Light grey decorative pattern background"></div>
    <div class="ribbon ribbon-top"></div>
    <div class="ribbon ribbon-bottom"></div>
    <div class="ribbon-fold fold-tl"></div>
    <div class="ribbon-fold fold-tr"></div>
    <div class="ribbon-fold fold-bl"></div>
    <div class="ribbon-fold fold-br"></div>
    <div class="panel">
      <div class="edge-trim trim-top" role="img" aria-label="Zigzag border trim"></div>
      <div class="edge-trim trim-bottom" role="img" aria-label="Zigzag border trim"></div>
      <div class="ornament orn-1" role="img" aria-label="Flower ornament"></div>
      <div class="ornament orn-2" role="img" aria-label="Flower ornament"></div>
      <div class="ornament orn-3" role="img" aria-label="Flower ornament"></div>
      <div class="ornament orn-4" role="img" aria-label="Flower ornament"></div>
      <h1 class="brand-name">Brisa Pastry Mill</h1>
      <p class="tagline">EMPANADA WHOLESALERS</p>
    </div>
  </section>

  <section class="card card-back">
    <p class="offer-lead">First Trial Order</p>
    <p class="offer-free">FREE</p>
    <div class="pastry-art" role="img" aria-label="Illustration of an empanada goes here"></div>
    <p class="product product-above">Empanadas</p>
    <p class="product product-main">CURRY PUFF</p>
    <p class="product product-below">Spiral Puff</p>
    <p class="phone">555-214-7093</p>
    <p class="contact contact-web">www.brisapastry.example</p>
    <div class="social"><span class="social-mark"></span><span>@BRISAPASTRY</span></div>
    <p class="contact contact-mail">tobin@brisapastry.example</p>
  </section>
</body>
</html>
```